Business Card Design Project

Business card for law firm
Use existing logo
Must have:
Gordon P. Haskell
3721-C West 14th
Fairbrook, ST 78599
ghaskell@bvlawgroup.example
www.bvlawgroup.example
555-555-0143

Target Market(s)

Clients and potential clients, generally adult, business background

Industry/Entity Type

Business

Requirements
Must have
• Our logo, see below

```html
<!DOCTYPE html>
<html lang="en">
<head>
<meta charset="utf-8">
<title>Brandt Vance – Business Card</title>
<link rel="stylesheet" href="https://fonts.googleapis.com/css2?family=Cinzel:wght@400;700&display=swap">
<style>
  :root {
    --page-bg: #f3f3f3;
    --card-light: #ffffff;
    --card-dark: #221f1d;
    --ink-dark: #2a2a2a;
    --ink-muted: #555555;
    --mark-grey: #6e6e6e;
    --rule: #9a9a9a;
    --ink-light: #ffffff;
    --divider: #6a6663;
  }
  * { margin: 0; padding: 0; box-sizing: border-box; }
  html, body {
    width: 1200px;
    height: 1000px;
    overflow: hidden;
    background: var(--page-bg);
    font-family: "Cinzel", serif;
  }
  .card {
    position: absolute;
    left: 155px;
    top: 211px;
    width: 933px;
    height: 519px;
    background: var(--card-light);
    border: 1px solid #dcdcdc;
  }
  .brand {
    position: absolute;
    left: 66px;
    top: 109px;
  }
  .brand-square {
    position: absolute;
    left: 0;
    top: 0;
    width: 80px;
    height: 80px;
    background: var(--mark-grey);
  }
  .brand-name {
    position: absolute;
    left: 91px;
    top: -6px;
    white-space: nowrap;
    font-size: 56px;
    font-weight: 400;
    line-height: 1;
    letter-spacing: 2px;
    color: var(--ink-dark);
  }
  .brand-rule {
    position: absolute;
    left: 91px;
    top: 56px;
    width: 568px;
    height: 1px;
    background: var(--rule);
  }
  .brand-tagline {
    position: absolute;
    left: 92px;
    top: 61px;
    white-space: nowrap;
    font-size: 23px;
    line-height: 1;
    letter-spacing: 1px;
    color: var(--ink-muted);
  }
  .contact-band {
    position: absolute;
    left: 0;
    top: 282px;
    width: 100%;
    height: 237px;
    background: var(--card-dark);
    color: var(--ink-light);
  }
  .person-name {
    position: absolute;
    left: 72px;
    top: 48px;
    font-size: 23px;
    font-weight: 700;
    letter-spacing: 0.5px;
    line-height: 1;
  }
  .contact-group {
    position: absolute;
    top: 128px;
    font-size: 20px;
    line-height: 27px;
    letter-spacing: 0.5px;
    white-space: nowrap;
  }
  .contact-address { left: 72px; }
  .contact-phone { left: 352px; }
  .contact-online { left: 536px; font-size: 19px; letter-spacing: 0.2px; }
  .contact-online .web { letter-spacing: 2px; }
  .divider {
    position: absolute;
    top: 120px;
    width: 1px;
    height: 70px;
    background: var(--divider);
  }
  .divider-one { left: 321px; }
  .divider-two { left: 517px; }
</style>
</head>
<body>
  <div class="card">
    <div class="brand">
      <div class="brand-square"></div>
      <div class="brand-name">Brandt Vance</div>
      <div class="brand-rule"></div>
      <div class="brand-tagline">Attorneys and Counselor</div>
    </div>

    <div class="contact-band">
      <div class="person-name">GORDON P. HASKELL</div>

      <div class="contact-group contact-address">
        <div>3721-C West 14th</div>
        <div>Fairbrook,&nbsp; ST&nbsp; 78599</div>
      </div>
      <div class="divider divider-one"></div>

      <div class="contact-group contact-phone">
        <div>555-555-0143</div>
      </div>
      <div class="divider divider-two"></div>

      <div class="contact-group contact-online">
        <div>ghaskell@bvlawgroup.example</div>
        <div class="web">www.bvlawgroup.example</div>
      </div>
    </div>
  </div>
</body>
</html>
```